Pebble Grocer

Hope all is well!

Wanted to make business cards for my father. His name is Samir Haddad and owns convenience stores. I have attached logo :)

He does not want any title just simple name and phone. An email would be nice as well.

Samir Haddad
Cell: 413-555-0148
Store: 413-555-0192

Pebblegrocer518@mailnest.example

The design and style is totally up to you :) The colors we were looking for were the same as logo :)

```html
<!DOCTYPE html>
<html lang="en">
<head>
<meta charset="utf-8">
<title>Pebble Grocer – Business Cards</title>
<link rel="stylesheet" href="https://fonts.googleapis.com/css2?family=Montserrat:wght@700;800&family=Open+Sans:wght@400;600&display=swap">
<style>
  :root {
    --backdrop: #232323;
    --navy: #26377a;
    --navy-deep: #1f2d66;
    --logo-blue: #2a3f8f;
    --red: #ee2f3a;
    --charcoal: #1b1718;
    --white: #ffffff;
  }
  * { box-sizing: border-box; margin: 0; padding: 0; }
  html, body {
    width: 1200px; height: 780px; overflow: hidden;
    background: var(--backdrop);
  }
  .sheet {
    width: 1200px; height: 780px;
    display: flex; align-items: center; justify-content: center; gap: 48px;
  }
  .card {
    position: relative;
    width: 540px; height: 310px;
    border-radius: 22px;
    border-bottom: 5px solid var(--red);
    box-shadow: 0 14px 30px rgba(0,0,0,0.55);
    overflow: hidden;
  }
  /* Back side */
  .card--back {
    background: var(--navy);
    display: flex; align-items: center; justify-content: center;
  }
  .brand-emboss {
    display: flex; align-items: center; gap: 16px;
    font-family: "Montserrat", sans-serif; font-weight: 800;
    font-size: 46px; letter-spacing: 1px;
    color: var(--navy-deep);
  }
  .brand-emboss .brand-dot {
    width: 44px; height: 44px; border-radius: 50%;
    background: var(--navy-deep);
  }
  /* Front side */
  .card--front {
    background: var(--charcoal);
  }
  .brand {
    position: absolute; left: 34px; top: 0; bottom: 0;
    display: flex; align-items: center; gap: 10px;
    font-family: "Montserrat", sans-serif; font-weight: 800;
    font-size: 26px; color: var(--logo-blue);
  }
  .brand .brand-dot {
    width: 22px; height: 22px; border-radius: 50%;
    background: var(--red);
  }
  .divider {
    position: absolute; left: 264px; top: 78px;
    width: 1px; height: 150px; background: var(--red);
  }
  .contact {
    position: absolute; left: 284px; top: 86px; right: 16px;
  }
  .contact__name {
    font-family: "Montserrat", sans-serif; font-weight: 800;
    font-size: 22px; margin-bottom: 34px;
    color: var(--logo-blue);
  }
  .contact__name .surname { color: var(--red); }
  .contact__list { list-style: none; }
  .contact__item {
    display: flex; align-items: center; gap: 7px;
    font-family: "Open Sans", sans-serif; font-size: 12px;
    color: var(--white); line-height: 20px;
    white-space: nowrap;
  }
  .contact__item svg { flex: none; width: 12px; height: 12px; fill: var(--red); }
</style>
</head>
<body>
  <main class="sheet">
    <section class="card card--back" aria-label="Card back">
      <div class="brand-emboss"><span class="brand-dot"></span>Pebble Grocer</div>
    </section>

    <section class="card card--front" aria-label="Card front">
      <div class="brand"><span class="brand-dot"></span>Pebble Grocer</div>
      <div class="divider"></div>
      <div class="contact">
        <h1 class="contact__name">Samir <span class="surname">Haddad</span></h1>
        <ul class="contact__list">
          <li class="contact__item">
            <svg viewBox="0 0 12 12" aria-hidden="true"><path d="M3 0h6a1 1 0 0 1 1 1v10a1 1 0 0 1-1 1H3a1 1 0 0 1-1-1V1a1 1 0 0 1 1-1zm0.5 1.5v8h5v-8z"/></svg>
            413-555-0148 (Cell)
          </li>
          <li class="contact__item">
            <svg viewBox="0 0 12 12" aria-hidden="true"><path d="M2.4 0.5l2 2.4-1.2 1.4c0.7 1.6 2 2.9 3.6 3.6l1.4-1.2 2.4 2-1.3 2C5 10.4 1.6 7 0.4 1.8z"/></svg>
            413-555-0192 (Store)
          </li>
          <li class="contact__item">
            <svg viewBox="0 0 12 12" aria-hidden="true"><path d="M0 2h12v8H0zm1.2 1l4.8 3.4L10.8 3z"/></svg>
            Pebblegrocer518@mailnest.example
          </li>
        </ul>
      </div>
    </section>
  </main>
</body>
</html>
```